6"x9" Postcard Mailer

A 6"x9" Postcard mailer targeted to forensic laboratories to advertise or mock forensic samples (https://veltrasync.example/products/mock-forensic-samples/).

Here is some copy, but we can modify if there is not enough space:

Headline:
Expedite Training, Validation, & R&D with Our Ready-to-Use Mock Samples

Bullet Points:

- Wide Variety of Sample Types: IRB-approved samples mimicking crime scene substances, including semen, hair, bone, saliva, blood, and vaginal epithelial cells.
- Diverse Scenarios: Simulate sexual assault and degraded samples for varied conditions.
- Custom Solutions: Tailored DNA quantities and concentrations to suit your lab's needs.

Use discount code PRAX47 for a 10% discount

```html
<!DOCTYPE html>
<html lang="en">
<head>
<meta charset="utf-8">
<title>Veltrasync Mock Samples Postcard</title>
<link href="https://fonts.googleapis.com/css2?family=League+Gothic&family=Antonio:wght@200;700&family=Roboto:wght@400&family=Montserrat:wght@400;800&display=swap" rel="stylesheet">
<style>
  :root {
    --stage: #606060;
    --paper: #ffffff;
    --blue-light: #2a8fd2;
    --blue-dark: #27539b;
    --rule-grey: #a7a9ac;
    --text-on-blue: #ffffff;
  }
  * { margin: 0; padding: 0; box-sizing: border-box; }
  html, body { width: 1200px; height: 626px; overflow: hidden; }
  body { background: var(--stage); position: relative; }

  .card { position: absolute; width: 527px; height: 345px; background: var(--paper); overflow: hidden; }
  .card--front { left: 62px; top: 132px; }
  .card--back { left: 605px; top: 134px; }
  .card-art { position: absolute; inset: 0; width: 527px; height: 345px; }

  .headline { position: absolute; right: 27px; text-align: right; font-family: "League Gothic", "Arial Narrow", sans-serif; line-height: 1; white-space: nowrap; font-weight: 400; }
  .headline__lead { font-size: 28.5px; color: var(--blue-light); }
  .headline__lead--one { top: 21px; }
  .headline__lead--two { top: 47px; }
  .headline__product { top: 71px; font-size: 44.5px; color: var(--blue-dark); }

  .features { position: absolute; right: 38px; top: 125px; text-align: right; color: var(--text-on-blue); font-family: "Roboto", Arial, sans-serif; font-size: 10.6px; line-height: 12.6px; white-space: nowrap; }
  .features p + p { margin-top: 11.5px; }

  .offer { position: absolute; right: 28px; text-align: right; white-space: nowrap; line-height: 1; }
  .offer__code-line { top: 272px; font-family: "Antonio", "Arial Narrow", sans-serif; font-weight: 200; font-size: 23.5px; letter-spacing: -0.2px; color: var(--blue-light); }
  .offer__code { font-weight: 700; color: var(--blue-dark); }
  .offer__amount { top: 299px; font-family: "Montserrat", Arial, sans-serif; font-weight: 800; font-size: 33px; color: var(--blue-dark); }

  .contact { position: absolute; left: 30px; top: 172px; color: var(--text-on-blue); }
  .contact__title { font-family: "League Gothic", "Arial Narrow", sans-serif; font-weight: 400; font-size: 31px; line-height: 1; letter-spacing: 0.3px; }
  .contact__list { list-style: none; margin-top: 7px; font-family: "Montserrat", Arial, sans-serif; font-size: 13px; line-height: 15px; }
  .contact__item { position: relative; padding-left: 23px; margin-bottom: 9.5px; white-space: nowrap; }
  .contact__icon { position: absolute; left: 1px; top: 1px; width: 14px; height: 14px; }
  .contact__item--address .contact__icon { top: 2px; }
</style>
</head>
<body>

<section class="card card--front" aria-label="Postcard front">
  <svg class="card-art" viewBox="0 0 527 345">
    <defs>
      <linearGradient id="photoTone" x1="0" y1="0" x2="0.6" y2="1">
        <stop offset="0" stop-color="#0b0d14"/>
        <stop offset="0.35" stop-color="#2a55c4"/>
        <stop offset="0.65" stop-color="#b9c1cf"/>
        <stop offset="1" stop-color="#f1eff0"/>
      </linearGradient>
    </defs>
    <rect class="feature-band" x="200" y="116" width="326" height="146" fill="var(--blue-light)"/>
    <line x1="240" y1="113" x2="527" y2="113" stroke="var(--blue-light)" stroke-width="2"/>
    <line x1="220" y1="265" x2="527" y2="265" stroke="var(--blue-light)" stroke-width="2"/>
    <path class="frame" d="M175 6.5 H520.5 V339 H100" fill="none" stroke="var(--blue-dark)" stroke-width="1"/>
    <circle cx="40" cy="160" r="219" fill="var(--blue-light)"/>
    <circle cx="40" cy="160" r="215" fill="var(--blue-dark)"/>
    <circle cx="40" cy="160" r="208" fill="var(--paper)"/>
    <circle cx="40" cy="160" r="203" fill="url(#photoTone)" role="img" aria-label="Photo: gloved hands swabbing a red blood spatter on a white surface with a cotton swab"/>
  </svg>

  <div class="headline headline__lead headline__lead--one">EXPEDITE TRAINING, VALIDATION</div>
  <div class="headline headline__lead headline__lead--two">&amp; R&amp;D WITH OUR READY-TO-USE</div>
  <h1 class="headline headline__product">MOCK SAMPLES</h1>

  <div class="features">
    <p>Wide Variety of Sample Types: IRB-approved<br>samples&nbsp; mimicking crime scene substances,<br>including&nbsp; semen, hair, bone, saliva, blood,<br>and vaginal&nbsp; epithelial cells.</p>
    <p>Diverse Scenarios: Simulate sexual assault and<br>degraded samples for varied conditions.</p>
    <p>Custom Solutions: Tailored DNA quantities and<br>concentrations to suit your lab's needs.</p>
  </div>

  <div class="offer offer__code-line">Use discount code <span class="offer__code">PRAX47</span> for a</div>
  <div class="offer offer__amount">10% DISCOUNT</div>
</section>

<section class="card card--back" aria-label="Postcard back">
  <svg class="card-art" viewBox="0 0 527 345">
    <g class="address-lines" stroke="var(--rule-grey)" stroke-width="0.6">
      <line x1="59" y1="58" x2="441" y2="58"/>
      <line x1="59" y1="87" x2="441" y2="87"/>
      <line x1="59" y1="115.5" x2="441" y2="115.5"/>
      <line x1="177" y1="144" x2="441" y2="144"/>
      <line x1="239" y1="173" x2="441" y2="173"/>
    </g>
    <circle cx="78" cy="364" r="224" fill="var(--blue-light)"/>
    <circle cx="78" cy="364" r="219" fill="var(--blue-dark)"/>
    <circle cx="78" cy="364" r="212" fill="var(--paper)"/>
    <circle cx="78" cy="364" r="208" fill="var(--blue-light)"/>
  </svg>

  <div class="contact">
    <h2 class="contact__title">CONTACT US:</h2>
    <ul class="contact__list">
      <li class="contact__item">
        <svg class="contact__icon" viewBox="0 0 16 16"><path d="M3.6 1.2l2.3 2.6-1.3 1.9c.9 2 2.6 3.8 4.7 4.8l1.9-1.3 2.6 2.3-1.4 2.5C7.4 14.3 1.7 8.6 1.7 3z" fill="var(--text-on-blue)"/></svg>
        +1 555 014 2290
      </li>
      <li class="contact__item">
        <svg class="contact__icon" viewBox="0 0 16 16" fill="none" stroke="var(--text-on-blue)" stroke-width="1.2"><circle cx="8" cy="9" r="6"/><ellipse cx="8" cy="9" rx="2.6" ry="6"/><line x1="2" y1="9" x2="14" y2="9"/><line x1="3" y1="6" x2="13" y2="6"/><line x1="3" y1="12" x2="13" y2="12"/></svg>
        info@veltrasync.example
      </li>
      <li class="contact__item">
        <svg class="contact__icon" viewBox="0 0 16 16"><rect x="1" y="3.5" width="14" height="9.5" fill="var(--text-on-blue)"/><path d="M1.5 4l6.5 5 6.5-5M1.5 12.5l5-4.2M14.5 12.5l-5-4.2" fill="none" stroke="var(--blue-light)" stroke-width="1"/></svg>
        veltrasync.example
      </li>
      <li class="contact__item contact__item--address">
        <svg class="contact__icon" viewBox="0 0 16 16"><path d="M8 1a5 5 0 0 0-5 5c0 3.6 5 9.5 5 9.5s5-5.9 5-9.5a5 5 0 0 0-5-5zm0 7a2 2 0 1 1 0-4 2 2 0 0 1 0 4z" fill="var(--text-on-blue)"/></svg>
        Lakeview Research Park<br>4180 Harbor Crest Drive, #210<br>Port Alden, LA 70999
      </li>
    </ul>
  </div>
</section>

</body>
</html>
```